Membership Drive "CHRISTMAS SPECIAL"

Looking to run a "Christmas Special" on 6 month Memberships for December 2019 to boost membership number up. This is a great time to get people exercising and everyone loves a Christmas Sale. Special is designed to attract more people to join and enjoy the savings.
Artwork will be display via social media (FB and Instagram) as well as in store. Artwork must be eye catching and direct to the customer. Customer should feel a sense of relief with being able to exercise at a lower cost .

Heading: "Christmas Sale"
6 Months
$199.00 Save over 30%
Terms and conditions apply"
*Offer End 31st December

below are other promos we had designed on Sketch Harbor along with potential photos to be included into this promo

Target Market(s)

Males and Females aged between 16 - 45

Industry/Entity Type

Fitness

Colors

Designer to choose colors to be used in the design.

Requirements
Must have
• Must emphasize "Christmas Special" $199.00 Save over 30%
• Terms and conditions apply
• Offer Ends 31st of December
• "All of our contact details"
• Address: 14 Wattle Rd Brindle Park 3187
• Ph: 9472 6158
• www.ironpulsefit.com.au
• Design format must come in PDF for a AO poster and an Instagram format please
Nice to have
• Some Christmas feels to the artwork

```html
<!DOCTYPE html>
<html lang="en">
<head>
<meta charset="utf-8">
<title>Christmas Sale Poster</title>
<link rel="stylesheet" href="https://fonts.googleapis.com/css2?family=Lobster&display=swap">
<style>
  :root {
    --stage: #e4e4e4;
    --sale-red: #a00000;
    --ink-red: #a3001a;
    --white: #ffffff;
    --icon-dark: #111111;
    --sky-light: #eef6fc;
    --sky-mid: #b4cde9;
    --sky-deep: #7193c6;
    --gift-purple: #b48ee6;
    --flake-pink: #e07a78;
    --portrait-light: #e8c7b0;
    --portrait-mid: #a8704c;
    --portrait-dark: #5c3a26;
  }
  * { box-sizing: border-box; margin: 0; padding: 0; }
  html, body {
    width: 1200px;
    height: 800px;
    overflow: hidden;
    background: var(--stage);
  }
  .stage { position: relative; width: 1200px; height: 800px; }
  .poster {
    position: absolute;
    left: 330px; top: 20px;
    width: 540px; height: 760px;
    overflow: hidden;
    font-family: 'Lobster', cursive;
    background: linear-gradient(180deg, var(--sky-light) 0%, var(--sky-mid) 55%, var(--sky-deep) 100%);
    box-shadow: 0 6px 18px rgba(0,0,0,0.25);
  }
  .hero-sky {
    position: absolute;
    left: 0; top: 0;
    width: 540px; height: 350px;
    background: radial-gradient(ellipse at 35% 45%, var(--sky-light) 0%, var(--sky-mid) 65%, var(--sky-deep) 100%);
  }
  .hero-photo {
    position: absolute;
    left: 106px; top: 0;
    width: 412px; height: 350px;
    background:
      radial-gradient(ellipse 46% 30% at 48% 14%, rgba(255,255,255,0.95) 0%, rgba(255,255,255,0) 100%),
      radial-gradient(ellipse 50% 58% at 52% 52%, var(--portrait-light) 0%, var(--portrait-mid) 55%, rgba(92,58,38,0) 100%),
      radial-gradient(ellipse 30% 22% at 36% 92%, rgba(200,20,30,0.85) 0%, rgba(200,20,30,0) 100%);
  }
  .decor {
    position: absolute;
    border-radius: 50%;
    background: radial-gradient(circle, rgba(255,255,255,0.9) 0%, rgba(255,255,255,0.35) 55%, rgba(255,255,255,0) 72%);
  }
  .decor-faint {
    background: radial-gradient(circle, rgba(255,255,255,0.6) 0%, rgba(255,255,255,0.2) 55%, rgba(255,255,255,0) 72%);
  }
  .decor-red {
    background: radial-gradient(circle, rgba(224,122,120,0.9) 0%, rgba(224,122,120,0.4) 55%, rgba(224,122,120,0) 72%);
  }
  .decor-gift {
    position: absolute;
    border-radius: 4px;
    background: linear-gradient(160deg, var(--gift-purple) 0%, rgba(180,142,230,0.7) 100%);
  }
  .flake-top-left { left: 0; top: 0; width: 76px; height: 76px; }
  .flake-top-right { left: 435px; top: 0; width: 105px; height: 105px; }
  .flake-mid-left { left: 0; top: 240px; width: 107px; height: 107px; }
  .flake-band-edge { left: 395px; top: 288px; width: 96px; height: 96px; z-index: 2; }
  .flake-band-red { left: 41px; top: 416px; width: 105px; height: 105px; z-index: 2; }
  .flake-wheel-left { left: 0; top: 508px; width: 56px; height: 83px; z-index: 2; }
  .flake-phone { left: 172px; top: 639px; width: 57px; height: 57px; }
  .flake-bottom { left: 238px; top: 696px; width: 92px; height: 66px; }
  .flake-bottom-right { left: 496px; top: 643px; width: 44px; height: 88px; }
  .gift-left { left: 0; top: 118px; width: 56px; height: 76px; transform: rotate(-14deg); }
  .gift-right { left: 478px; top: 500px; width: 64px; height: 82px; transform: rotate(-14deg); z-index: 2; }
  .sale-band {
    position: absolute;
    left: 0; top: 350px;
    width: 540px; height: 184px;
    background: var(--sale-red);
    color: var(--white);
    z-index: 1;
  }
  .sale-title {
    position: absolute;
    left: 26px; top: 0;
    font-size: 56px;
    line-height: 1.2;
    font-weight: 400;
  }
  .sale-price {
    position: absolute;
    left: 194px; top: 68px;
    font-size: 44px;
    line-height: 1.2;
  }
  .sale-saving {
    position: absolute;
    left: 154px; top: 134px;
    font-size: 31px;
    line-height: 1.2;
  }
  .sale-term {
    position: absolute;
    left: 420px; top: 42px;
    width: 94px;
    text-align: center;
    line-height: 1;
  }
  .sale-term-number { display: block; font-size: 74px; }
  .sale-term-unit { display: block; font-size: 26px; margin-top: 0; }
  .contact {
    position: absolute;
    color: var(--ink-red);
    text-align: center;
    white-space: nowrap;
    z-index: 3;
  }
  .contact-icon { display: block; margin: 0 auto 4px; }
  .contact-address { left: 120px; top: 545px; width: 304px; font-size: 19px; }
  .contact-phone { left: 52px; top: 614px; width: 120px; font-size: 19px; }
  .contact-web { left: 270px; top: 617px; width: 240px; font-size: 18px; }
  .fine-print {
    position: absolute;
    top: 720px;
    color: var(--ink-red);
    font-size: 17px;
    white-space: nowrap;
    z-index: 3;
  }
  .fine-terms { left: 14px; }
  .fine-offer { right: 18px; }
</style>
</head>
<body>
<main class="stage">
  <article class="poster">
    <div class="hero-sky"></div>
    <div class="hero-photo" role="img" aria-label="Photo of a smiling woman in a Santa hat holding a red and white gift box"></div>

    <div class="decor flake-top-left" role="img" aria-label="White snowflake ornament"></div>
    <div class="decor decor-faint flake-top-right" role="img" aria-label="Faint snowflake ornament"></div>
    <div class="decor decor-faint flake-mid-left" role="img" aria-label="Faint snowflake ornament"></div>
    <div class="decor-gift gift-left" role="img" aria-label="Purple gift box ornament"></div>

    <section class="sale-band">
      <h1 class="sale-title">Christmas Sale</h1>
      <p class="sale-price">$ 199.00</p>
      <p class="sale-saving">Save Over 30%</p>
      <p class="sale-term"><span class="sale-term-number">6</span><span class="sale-term-unit">Months</span></p>
    </section>

    <div class="decor flake-band-edge" role="img" aria-label="White snowflake ornament"></div>
    <div class="decor decor-red flake-band-red" role="img" aria-label="Pink snowflake ornament"></div>
    <div class="decor flake-wheel-left" role="img" aria-label="White snowflake ornament"></div>
    <div class="decor-gift gift-right" role="img" aria-label="Purple gift box ornament"></div>
    <div class="decor decor-faint flake-phone" role="img" aria-label="Faint snowflake ornament"></div>
    <div class="decor flake-bottom" role="img" aria-label="White snowflake ornament"></div>
    <div class="decor decor-faint flake-bottom-right" role="img" aria-label="Faint snowflake ornament"></div>

    <div class="contact contact-address">
      <svg class="contact-icon" width="26" height="38" viewBox="0 0 26 38" aria-hidden="true">
        <path d="M13 1C6.4 1 1 6.2 1 12.8 1 21.5 13 37 13 37s12-15.5 12-24.2C25 6.2 19.6 1 13 1z" fill="var(--icon-dark)"/>
        <circle cx="13" cy="12.5" r="5" fill="var(--sky-mid)"/>
      </svg>
      14 Wattle Rd Brindle Park 3187
    </div>

    <div class="contact contact-phone">
      <svg class="contact-icon" width="22" height="40" viewBox="0 0 22 40" aria-hidden="true">
        <rect x="1" y="1" width="20" height="38" rx="3" fill="var(--icon-dark)"/>
        <rect x="3.5" y="6" width="15" height="25" fill="var(--white)"/>
        <circle cx="11" cy="35" r="2" fill="var(--white)"/>
      </svg>
      9472 6158
    </div>

    <div class="contact contact-web">
      <svg class="contact-icon" width="40" height="40" viewBox="0 0 40 40" aria-hidden="true">
        <circle cx="20" cy="20" r="19" fill="var(--icon-dark)"/>
        <g stroke="var(--sky-mid)" stroke-width="2" fill="none">
          <ellipse cx="20" cy="20" rx="8" ry="19"/>
          <line x1="20" y1="1" x2="20" y2="39"/>
          <line x1="1" y1="20" x2="39" y2="20"/>
          <line x1="4" y1="11" x2="36" y2="11"/>
          <line x1="4" y1="29" x2="36" y2="29"/>
        </g>
      </svg>
      www.ironpulsefit.com.au
    </div>

    <p class="fine-print fine-terms">Terms and conditions apply</p>
    <p class="fine-print fine-offer">Offer End 31st December</p>
  </article>
</main>
</body>
</html>
```